Web Design Project

We are looking for a new site design for the OLVEN Summit & Fair. The current site can be found at
http://olvenmeetup-example.org/
The URL is provided for reference. We want a completely different look and layout which is shown in the specifications document.
As part of the design, we want a home page, inside page and a mobile design. The mobile version is to be fairly simple and uncluttered and based on the web design - simple is key and a sample site is referenced in the specifications document.
The design you provide will be implemented in Joomla. The design winner will only need to provide the PSD or Fireworks PNG format. We anticipate creating the template coding in-house.
However, if you have experience creating Joomla templates, please let us know as we may ask you to bid separately to do that phase of the project.
We've provided a specifications document which includes wireframes of the home page, inside page, and mobile version as well as sample sites. We've also included logo files and a picture of the conference city.
For the header at the top, as indicated in the specs document, we want to keep the same overall treatment to every page. We don't want to include images from the city within the header. Instead we want a graphic treatment with the logo. In this manner, the design will be flexiable and can be used for future years.
For the home page, we've indicated that we'd like to have a banner placement implemented within the design. Please place the city image in this area with a nice graphic treatment. This might also be a good place to include the hosting city and date: Saskatoon, SK June 2-5. 2013
The wireframe is provided to illustrate the placement of content and menu items. The exact dimensions of each component can be revised as you see fit. We are also flexiable if you feel we have missed items.

```html
<!DOCTYPE html>
<html lang="en">
<head>
<meta charset="utf-8">
<title>OLVEN Summit &amp; Fair</title>
<link href="https://fonts.googleapis.com/css2?family=Libre+Baskerville:wght@400;700&family=Tinos&family=Arimo:wght@400;700&family=Ubuntu:wght@700&display=swap" rel="stylesheet">
<style>
:root{
  --blue:#0b4f9c;
  --blue-dark:#063d7e;
  --red:#e02128;
  --red-dark:#b8141a;
  --page:#efefef;
  --text:#4a4a4a;
  --white:#fff;
  --grey-band:#ececec;
}
*{box-sizing:border-box;margin:0;padding:0}
html,body{width:1200px;height:1125px;overflow:hidden}
body{background:var(--page);font-family:"Tinos",serif;position:relative}
.top-bar{position:absolute;left:0;top:0;width:1200px;height:8px;background:var(--blue)}
.site{position:absolute;left:131px;top:0;width:938px;height:1125px}
.brand{position:absolute;left:0;top:30px;display:flex;align-items:center;gap:12px}
.brand-mark{width:44px;height:44px;border-radius:50%;background:var(--blue)}
.brand-name{font-family:"Libre Baskerville",serif;font-weight:700;font-size:22px;color:var(--blue);line-height:1.2}
.brand-name small{display:block;font-size:12px;font-weight:700;color:var(--blue)}
.contact{position:absolute;right:0;top:72px;display:flex;align-items:center}
.contact-icon{width:42px;height:44px;border-radius:5px;background:linear-gradient(#e63037,var(--red-dark));display:flex;align-items:center;justify-content:center;box-shadow:0 2px 3px rgba(0,0,0,.3)}
.contact-rule{width:1px;height:48px;background:#ccc;margin:0 16px}
.contact-text{font-family:"Ubuntu",sans-serif;font-weight:700;line-height:1}
.contact-text .q{color:var(--blue);font-size:23px}
.contact-text .num{color:var(--red);font-size:26px;margin-top:3px}
.main-nav{position:absolute;left:0;top:192px;width:938px;height:42px;display:flex;background:linear-gradient(var(--blue),var(--blue-dark))}
.main-nav a{display:flex;align-items:center;justify-content:center;color:var(--white);text-decoration:none;font-family:"Libre Baskerville",serif;font-size:14px;border-right:1px solid #2d66ab}
.main-nav a.active{background:var(--red)}
.banner{position:absolute;left:0;top:234px;width:938px;height:300px;background:linear-gradient(180deg,#b9c3cf 0%,#d7cfc4 30%,#a49578 55%,#5d6b6e 75%,#3e4f47 100%)}
.slide-dots{position:absolute;right:10px;bottom:8px;display:flex;gap:3px}
.slide-dots span{width:10px;height:10px;background:var(--white)}
.slide-dots span.on{background:var(--blue)}
.mailing{position:absolute;left:0;top:334px;width:251px;height:200px;background:rgba(11,79,156,.92)}
.mailing h2{position:absolute;left:0;top:13px;width:100%;font-family:"Libre Baskerville",serif;font-weight:400;font-size:14px;white-space:nowrap;color:var(--white);text-align:center}
.mailing .field{position:absolute;left:20px;width:211px;height:39px;background:var(--white);border:1px solid #ccc;box-shadow:inset 0 2px 4px rgba(0,0,0,.2)}
.mailing .field.first{top:46px}
.mailing .field.second{top:93px}
.mailing .submit{position:absolute;left:20px;top:141px;width:211px;height:38px;background:linear-gradient(#e83038,var(--red-dark));border:1px solid var(--white);color:var(--white);font-family:"Libre Baskerville",serif;font-size:12.5px;white-space:nowrap;display:flex;align-items:center;justify-content:center}
.quick-links{position:absolute;left:0;top:534px;width:251px;height:284px;background:var(--red)}
.quick-links h2{height:54px;display:flex;align-items:center;justify-content:center;font-family:"Libre Baskerville",serif;font-weight:400;font-size:22px;color:var(--white);background:linear-gradient(#e83038,#c8161d)}
.quick-links ul{list-style:none}
.quick-links li{height:38px;display:flex;align-items:center;padding-left:22px;border-bottom:1px dotted #f08a8d;color:var(--white);font-family:"Libre Baskerville",serif;font-size:13px;white-space:nowrap}
.quick-links li::before{content:"";border-left:8px solid var(--white);border-top:5px solid transparent;border-bottom:5px solid transparent;margin-right:12px}
.weather{position:absolute;left:0;top:818px;width:251px;height:146px;background:var(--white);border:1px solid #ddd}
.weather .today{position:absolute;left:100px;top:12px;width:140px;font-family:"Arimo",sans-serif;font-size:11px;line-height:13px;color:#222}
.weather .temp{font-size:20px;line-height:22px;color:#1d4f7c;font-weight:700;margin-top:4px}
.weather .temp sup{font-size:11px}
.weather .tomorrow{position:relative;font-size:9px;line-height:11px;color:#444;margin-top:4px;padding-left:38px;border-top:1px solid #ddd;padding-top:4px}
.weather .tomorrow b{display:block;font-size:13px;line-height:15px;color:#999;margin-top:2px}
.weather .tomorrow sup{font-size:8px}
.weather .days{position:absolute;left:0;bottom:0;width:100%;height:47px;display:flex;background:#f4f4f4;border-top:1px solid #ddd}
.weather .day{flex:1;border-right:1px solid #ddd;font-family:"Arimo",sans-serif;font-size:9px;color:#888;padding:8px 0 0 14px;position:relative}
.weather .day b{display:block;font-size:14px;color:#aaa;margin-top:2px}
.weather .day b sup{font-size:8px}
.weather .day svg{position:absolute;right:5px;top:20px}
.social{position:absolute;left:0;top:964px;width:251px;height:98px;background:var(--white);border:1px solid #ddd;text-align:center}
.social h2{font-family:"Libre Baskerville",serif;font-weight:400;font-size:18px;color:var(--blue);margin-top:16px}
.social .icons{display:flex;justify-content:center;gap:8px;margin-top:12px}
.social .icons span{width:30px;height:30px;border-radius:3px;background:var(--blue)}
.social .icons span:nth-child(2){background:#4aa8d8}
.social .icons span:nth-child(4),.social .icons span:nth-child(5){background:#e66a17}
.welcome{position:absolute;left:251px;top:534px;width:687px;height:338px;background:var(--white)}
.welcome h1,.sponsors h2{height:54px;display:flex;align-items:center;padding-left:24px;font-family:"Libre Baskerville",serif;font-weight:400;font-size:22px;color:var(--white)}
.welcome h1{background:linear-gradient(var(--blue),var(--blue-dark))}
.welcome p{font-size:13px;line-height:15.8px;letter-spacing:.35px;color:var(--text);text-align:justify;padding:0 27px 0 24px;margin-top:24px}
.welcome p+p{margin-top:16px}
.welcome .divider{position:absolute;left:20px;right:20px;bottom:24px;height:2px;background:linear-gradient(90deg,transparent,#aaa 50%,transparent)}
.sponsors{position:absolute;left:251px;top:872px;width:687px;height:120px}
.sponsors h2{background:var(--red)}
.sponsor-row{height:66px;background:var(--grey-band);display:flex;align-items:center;justify-content:space-around}
.sponsor-row span{width:92px;height:16px;background:#8a8a8a;border-radius:2px}
.site-footer{position:absolute;left:251px;top:992px;width:687px;height:70px;background:var(--blue);font-family:"Arimo",sans-serif;color:var(--white);text-align:right;padding:24px 18px 0 0}
.site-footer nav{font-size:12px}
.site-footer nav a{color:var(--white);text-decoration:none}
.site-footer p{font-size:10.5px;margin-top:8px}
</style>
</head>
<body>
<div class="top-bar"></div>
<div class="site">
  <header>
    <div class="brand">
      <span class="brand-mark"></span>
      <div class="brand-name">OLVEN<small>Summit &amp; Fair &middot; Saskatoon, SK June 2-5, 2013</small></div>
    </div>
    <div class="contact">
      <div class="contact-icon">
        <svg width="22" height="22" viewBox="0 0 24 24"><path fill="#fff" d="M6.6 10.8a15 15 0 0 0 6.6 6.6l2.2-2.2c.3-.3.7-.4 1-.2 1.1.4 2.3.6 3.6.6.6 0 1 .4 1 1V20c0 .6-.4 1-1 1A17 17 0 0 1 3 4c0-.6.4-1 1-1h3.5c.6 0 1 .4 1 1 0 1.3.2 2.5.6 3.6.1.3 0 .7-.2 1z"/></svg>
      </div>
      <div class="contact-rule"></div>
      <div class="contact-text"><div class="q">Have a question?</div><div class="num">(555) 014-2290</div></div>
    </div>
  </header>

  <nav class="main-nav">
    <a class="active" style="width:77px">HOME</a>
    <a style="width:98px">ABOUT</a>
    <a style="width:121px">SCHEDULE</a>
    <a style="width:150px">REGISTRATION</a>
    <a style="width:126px">EXHIBITORS</a>
    <a style="width:126px">EDUCATION</a>
    <a style="width:115px">SPONSORS</a>
    <a style="width:125px;border-right:0">CONNECT</a>
  </nav>

  <div class="banner" role="img" aria-label="Evening view of the host city skyline and river bridges">
    <div class="slide-dots"><span class="on"></span><span></span><span></span></div>
  </div>

  <section class="mailing">
    <h2>JOIN OUR MAILING LIST</h2>
    <div class="field first"></div>
    <div class="field second"></div>
    <div class="submit">CLICK HERE TO SUBMIT</div>
  </section>

  <section class="quick-links">
    <h2>QUICK LINKS</h2>
    <ul>
      <li>Lorem Ipsum Dolor Sit Amet</li>
      <li>Lorem Ipsum Dolor Sit Amet</li>
      <li>Lorem Ipsum Dolor Sit Amet</li>
      <li>Lorem Ipsum Dolor Sit Amet</li>
      <li>Lorem Ipsum Dolor Sit Amet</li>
      <li style="border-bottom:0">Lorem Ipsum Dolor Sit Amet</li>
    </ul>
  </section>

  <section class="weather">
    <svg style="position:absolute;left:16px;top:18px" width="64" height="64" viewBox="0 0 64 64"><circle cx="32" cy="32" r="30" fill="#f6d56a"/><circle cx="32" cy="32" r="26" fill="#fbb80f"/></svg>
    <div class="today">Today, Mon, July 18th, 2011
      <div class="temp">38<sup>o</sup> C <span style="color:#ccc">/</span> 124<sup>o</sup> F</div>
      <div class="tomorrow">
        <svg style="position:absolute;left:0;top:6px" width="32" height="22" viewBox="0 0 32 22"><ellipse cx="16" cy="11" rx="14" ry="8" fill="#ccc"/></svg>
        Tomorrow, Tuesday<b>38<sup>o</sup> C / 124<sup>o</sup> F</b>
      </div>
    </div>
    <div class="days">
      <div class="day">Wednesday<b>28<sup>o</sup> C</b><svg width="22" height="16"><ellipse cx="11" cy="8" rx="10" ry="6" fill="#ccc"/></svg></div>
      <div class="day">Thursday<b>30<sup>o</sup> C</b><svg width="22" height="16"><ellipse cx="11" cy="8" rx="10" ry="6" fill="#ddd"/></svg></div>
      <div class="day" style="border-right:0">Friday<b>27<sup>o</sup> C</b><svg width="22" height="16"><ellipse cx="11" cy="8" rx="10" ry="6" fill="#ddd"/></svg></div>
    </div>
  </section>

  <section class="social">
    <h2>STAY CONNECTED</h2>
    <div class="icons"><span></span><span></span><span></span><span></span><span></span></div>
  </section>

  <section class="welcome">
    <h1>WELCOME TO OLVEN NATIONAL SUMMIT</h1>
    <p>Lorem ipsum dolor sit amet, consectetur adipisicing elit, sed do eiusmod tempor incididunt ut labore et dolore magna aliqua. Ut enim ad minim veniam, quis nostrud exercitation ullamco laboris nisi ut aliquip ex ea commodo consequat. Duis aute irure dolor in reprehenderit in voluptate velit esse cillum dolore eu fugiat nulla pariatur. Excepteur sint occaecat cupidatat non proident, sunt in culpa qui officia deserunt mollit anim id est laborum.</p>
    <p>Sed ut perspiciatis unde omnis iste natus error sit voluptatem accusantium doloremque laudantium, totam rem aperiam, eaque ipsa quae ab illo inventore veritatis et quasi architecto beatae vitae dicta sunt explicabo. Nemo enim ipsam voluptatem quia voluptas sit aspernatur aut odit aut fugit, sed quia consequuntur magni dolores eos qui ratione voluptatem sequi nesciunt. Neque porro quisquam est, qui dolorem ipsum quia dolor sit amet, consectetur, adipisci velit, sed quia non numquam eius modi tempora incidunt ut labore et dolore magnam aliquam quaerat voluptatem. Ut enim ad minima veniam, quis nostrum exercitationem ullam corporis suscipit laboriosam.</p>
    <div class="divider"></div>
  </section>

  <section class="sponsors">
    <h2>OUR SPONSORS</h2>
    <div class="sponsor-row"><span></span><span></span><span></span><span></span><span></span></div>
  </section>

  <footer class="site-footer">
    <nav><a>Home</a> . <a>About</a> . <a>Schedule</a> . <a>Registration</a> . <a>Exhibitors</a> . <a>Education</a> . <a>Sponsors</a> . <a>Connect</a></nav>
    <p>Copyright &copy; 2012-2013 OLVEN National Summit, All Rights Reserved.</p>
  </footer>
</div>
</body>
</html>
```